Plakat-Design für Verkauf von Bio-zertifiziertem Saatgut
Zielgruppe
Wir sind ein Start Up und verkaufen BIO Zertifiziertes Saatgut für Gemüse, Kräuter, Heilpflanzen und essbare Sprossen etc. Zielgruppe ist vor allem die DIY Community von Jung bis Alt.
Aufgabenstellung
*** INFO*** Da es keine 'Kalender'-Projekte gibt, sollten wir das Projekt unter 'Plakat' einstellen ***INFO***
Wir sind auf der Suche nach einem Design für einen Monatskalender (Deckblatt, 12 Monate, Schlussblatt) der als ewiger Aussaatkalender fungieren soll (Keine Jahreszahlen, nur der Monat). Jeden Monat sollen die Sorten gezeigt werden die jetzt ausgesät werden können. Am Besten teilweise (nicht alle) als Illustrationen oder Bilder. Die Sorten orientieren sich an unserem Saatgutsortiment. Als Unterteilung kann man: 'Vorzucht im Haus', Frühbeet' und 'Direktsaat'
Die Informationen welche Samen wann ausgesät werden, kommen von uns. (Erstmal Platzhalter für das Design nutzen) Falls der Designer Erfahrung in diesem Bereich hat, kann er die Informationen auch selber einfügen. Sonst ist der Designer für Layout und Illustrationen/Bilder zuständig. Toll wäre wenn für jeden Monat noch eine 'Bauernweisheit' zum Thema Pflanzen / Aussaat / Garten hinzugefügt werden kann.
Das Design soll sich an unserer CI der Website www.keimfeld.de orientieren. Logo, Farben und Fonts (My-Everything, BW Mitga) sind im Anhang beigefügt. Auch die Vorlage der Druckerei ist beigefügt. Format: DIN A4 hoch (210 x 297 mm), beidseitig bedruckt so das man den Kalender auch Aufgeklappt nutzen kann.
Falls noch Informationen benötigt werden, dann meldet euch gerne!

```html
<!DOCTYPE html>
<html lang="de">
<head>
<meta charset="utf-8">
<title>Aussaat-Kalender – Keimfeld</title>
<link rel="stylesheet" href="https://fonts.googleapis.com/css2?family=Allura&family=Mulish:wght@400;600;800&display=swap">
<style>
  :root{
    --bg:#a4b5b8;
    --green:#6b9a3b;
    --green-dark:#5a8430;
    --brown:#6e4b22;
    --sage:#dde2d3;
    --sage-row:#c7cfb6;
    --paper:#ebe7de;
    --panel:rgba(236,236,232,.86);
    --ink:#4a4a40;
  }
  *{box-sizing:border-box;margin:0;padding:0}
  html,body{width:1200px;height:882px;overflow:hidden}
  body{background:var(--bg);font-family:'Mulish',sans-serif;color:var(--ink);position:relative}
  .sheet{position:absolute;overflow:hidden;box-shadow:0 3px 10px rgba(0,0,0,.18)}

  /* Cover */
  .cover{left:91px;top:155px;width:416px;height:590px}
  .cover-photo{position:absolute;inset:0;
    background:
      radial-gradient(circle at 82% 32%,#d33a22 0 14%,transparent 30%),
      radial-gradient(circle at 25% 82%,#c8281c 0 12%,transparent 26%),
      radial-gradient(circle at 62% 86%,#8a2d55 0 10%,transparent 22%),
      radial-gradient(circle at 85% 70%,#5f8f35 0 12%,transparent 26%),
      radial-gradient(circle at 50% 60%,#cf6a33 0 10%,transparent 24%),
      linear-gradient(135deg,#5b3e2a 0%,#6a4a33 35%,#a2452b 60%,#4f7a2c 100%)}
  .cover-panel{position:absolute;left:0;top:64px;width:200px;height:241px;background:var(--panel);border-radius:0 10px 10px 0}
  .brand{position:absolute;left:0;right:0;top:24px;text-align:center;color:var(--green);font-weight:600;font-size:11px;letter-spacing:2px}
  .brand-dot{display:block;width:30px;height:30px;border-radius:50%;background:var(--green);margin:0 auto 8px}
  .cover-title{position:absolute;left:18px;top:101px;color:var(--green);font-weight:800;font-size:28px;line-height:34px;letter-spacing:.5px}
  .cover-rule{position:absolute;left:0;top:176px;width:200px;height:2px;background:var(--green)}
  .cover-sub{position:absolute;left:18px;top:188px;font-size:11px;line-height:16px;color:var(--brown)}

  /* Month back sheet */
  .month-back{left:550px;top:159px;width:414px;height:589px;background:var(--sage)}
  .section-title{position:absolute;left:0;width:205px;top:93px;text-align:center;color:var(--green);font-weight:800;font-size:12px;letter-spacing:.5px}
  .section-icon{position:absolute;left:66px;top:111px;width:74px;height:37px;border-radius:37px 37px 0 0;background:var(--sage-row)}
  .sow-table{position:absolute;left:28px;top:148px;border-collapse:separate;border-spacing:2px 1px;font-size:9px}
  .sow-table td{width:73px;height:15px;padding-left:5px;background:var(--sage-row);color:var(--ink)}
  .sow-table td.empty{background:transparent}
  .veg-art{position:absolute;left:85px;top:390px;width:110px;height:70px;border-radius:40px;background:linear-gradient(160deg,#7fa893,#3e6b5a);transform:rotate(-20deg)}
  .paper-foot{position:absolute;left:0;bottom:0;width:414px;height:118px}
  .month-script{position:absolute;font-family:'Allura',cursive;color:var(--green);line-height:1}
  .back-script{left:32px;top:482px;font-size:58px}
  .back-label{position:absolute;left:70px;top:551px;color:var(--brown);font-weight:800;font-size:15px}
  .seeds{position:absolute;border-radius:50%;background:radial-gradient(circle,#b39a78 0 35%,rgba(179,154,120,0) 70%)}
  .back-seeds{left:185px;top:540px;width:170px;height:50px}
  .foot-brand{position:absolute;left:348px;top:560px;display:flex;align-items:center;gap:4px;font-size:9px;font-weight:600;color:var(--green)}
  .foot-brand i{width:12px;height:12px;border-radius:50%;background:var(--green)}

  /* Month front sheet */
  .month-front{left:742px;top:109px;width:414px;height:585px;background:var(--paper)}
  .front-script{left:28px;top:44px;font-size:80px}
  .front-seeds{left:215px;top:0;width:200px;height:95px}
  .garden-photo{position:absolute;left:0;top:0;width:414px;height:585px}
  .info-panel{position:absolute;left:0;top:183px;width:191px;height:104px;background:var(--panel);border-radius:0 10px 10px 0;padding:13px 12px 0 16px}
  .info-panel h2{font-size:9px;font-weight:800;color:var(--brown);letter-spacing:.3px;margin-bottom:8px}
  .info-panel p{font-size:6.6px;line-height:8.4px;color:var(--ink)}
</style>
</head>
<body>

<section class="sheet cover">
  <div class="cover-photo" role="img" aria-label="Frisches Gemüse auf Holztisch: Tomaten, Chilis, Paprika, Karotten, Zwiebeln, Radicchio"></div>
  <div class="cover-panel">
    <div class="brand"><span class="brand-dot"></span>KEIMFELD</div>
    <h1 class="cover-title">AUSSAAT-<br>KALENDER</h1>
    <div class="cover-rule"></div>
    <p class="cover-sub">Saisonkalender<br>für Gemüse und Kräuter</p>
  </div>
</section>

<section class="sheet month-back">
  <h2 class="section-title">DIREKTSAAT</h2>
  <div class="section-icon"></div>
  <table class="sow-table">
    <tr><td>Radieschen</td><td>Radieschen</td></tr>
    <tr><td>Aubergine</td><td>Aubergine</td></tr>
    <tr><td>Gurke</td><td>Gurke</td></tr>
    <tr><td>Kopfsalat</td><td>Kopfsalat</td></tr>
    <tr><td>Blumenkohl</td><td>Blumenkohl</td></tr>
    <tr><td>Brokkoli</td><td>Brokkoli</td></tr>
    <tr><td>Bohnen</td><td>Bohnen</td></tr>
    <tr><td>Aubergine</td><td>Aubergine</td></tr>
    <tr><td>Blumenkohl</td><td>Blumenkohl</td></tr>
    <tr><td>Gurke</td><td>Gurke</td></tr>
    <tr><td>Brokkoli</td><td>Brokkoli</td></tr>
    <tr><td>Radieschen</td><td>Radieschen</td></tr>
    <tr><td>Blumenkohl</td><td class="empty"></td></tr>
    <tr><td>Brokkoli</td><td class="empty"></td></tr>
    <tr><td>Kopfsalat</td><td class="empty"></td></tr>
  </table>
  <div class="veg-art" role="img" aria-label="Aquarell-Illustration einer Zucchini"></div>
  <svg class="paper-foot" viewBox="0 0 414 118" aria-hidden="true">
    <path fill="#ebe7de" d="M0 6 L30 2 L60 9 L95 4 L130 12 L165 8 L200 16 L240 10 L280 20 L320 14 L360 24 L414 20 L414 118 L0 118 Z"/>
  </svg>
  <div class="month-script back-script">Juli</div>
  <div class="back-label">Aussaat</div>
  <div class="seeds back-seeds" role="img" aria-label="Verstreute Saatkörner"></div>
  <div class="foot-brand"><i></i>Keimfeld</div>
</section>

<section class="sheet month-front">
  <svg class="garden-photo" viewBox="0 0 414 585" role="img" aria-label="Gärtner beim Hacken im Gemüsebeet, vorne ein Korb mit frisch geerntetem Gemüse">
    <defs>
      <linearGradient id="garden" x1="0" y1="0" x2="0" y2="1">
        <stop offset="0" stop-color="#a9c4d6"/>
        <stop offset=".18" stop-color="#6f9a48"/>
        <stop offset=".6" stop-color="#4f7f2c"/>
        <stop offset=".85" stop-color="#7a6a4a"/>
        <stop offset="1" stop-color="#5e7a34"/>
      </linearGradient>
    </defs>
    <path fill="url(#garden)" d="M0 150 L40 138 L80 142 L120 124 L160 128 L200 112 L240 118 L280 100 L330 104 L370 92 L414 96 L414 585 L0 585 Z"/>
  </svg>
  <div class="seeds front-seeds" role="img" aria-label="Verstreute Saatkörner"></div>
  <div class="month-script front-script">Juli</div>
  <div class="info-panel">
    <h2>UDANIS CUPTA DOLUT REM ET</h2>
    <p>Equamus sitatust, num as sim consedio. Et pore niscipi ciisquiae earum facearum cumeni ipsunt officiat fugitation etust, tection rem ut latur, corepellatem as et alit ex eveliquos as sunte omnis molutemo beat eostioribus, con nonectiorum, explita sumquos alignit perchitat reped exernat quam accus quatures il endelibus, conet litatur?</p>
  </div>
</section>

</body>
</html>
```